Velvor IT Services Business Card

Velvor IT Services are a Perth based IT Services company. We would like to incorporate our company logo (attached) and stick with the blue that is in that design. I would like a clean look design that isn't too busy, yet creates a lasting image that is instantly recognisable in the recipients mind.

Target Market(s)

The target audience is small/medium business owners.

Industry/Entity Type

Business

Font styles to use
Serif
Sans Serif

Colors

Designer to choose colors to be used in the design.

Requirements
Must have
• The design should include:
Business name: Velvor IT Services
Directors Name: Marcus Dredge
Phone Number: 0483 906 452
Email: support@velvorit.com.au
Website: www.velvorit.com.au

```html
<!DOCTYPE html>
<html lang="en">
<head>
<meta charset="utf-8">
<title>Velvor IT Services – Business Card</title>
<link rel="stylesheet" href="https://fonts.googleapis.com/css2?family=Arimo:wght@700&family=Questrial&display=swap">
<style>
  :root {
    --stage-centre: #a3a4a7;
    --stage-edge: #737477;
    --card-white: #ffffff;
    --band-grey: #d2d3d5;
    --band-square: #c3c4c6;
    --brand-blue: #1d4fa0;
    --brand-deep: #1a3f8f;
    --ink-grey: #3c3c3e;
    --tile-blue: #9aa5d6;
    --tile-light: #bfe6f7;
    --seam: #9c9d9f;
    --back-glow: #ffffff;
    --back-edge: #c4c5c7;
  }
  * { margin: 0; padding: 0; box-sizing: border-box; }
  html, body { width: 1200px; height: 1200px; overflow: hidden; }
  body {
    position: relative;
    background: radial-gradient(circle at 50% 45%, var(--stage-centre) 0%, var(--stage-edge) 75%);
    font-family: "Questrial", sans-serif;
  }
  .card { position: absolute; left: 218px; width: 765px; overflow: hidden; }

  /* Front */
  .card-front { top: 127px; height: 462px; background: var(--band-grey); }
  .front-header { position: absolute; left: 0; top: 0; width: 100%; height: 234px; background: var(--card-white); }
  .brand-name {
    position: absolute; left: 40px; top: 96px;
    display: flex; align-items: center; gap: 14px;
    color: var(--brand-blue); font-size: 34px; letter-spacing: 1px;
  }
  .brand-dot { width: 22px; height: 22px; border-radius: 4px; background: var(--brand-blue); }
  .tile { position: absolute; border-radius: 10px; }
  .tile-blue { background: linear-gradient(135deg, var(--tile-blue), var(--tile-light) 55%, var(--tile-blue)); opacity: .9; }
  .tile-grey { background: var(--band-square); }

  .contact-block { position: absolute; left: 441px; top: 252px; color: var(--ink-grey); }
  .role { font-size: 20px; }
  .person-name { font-family: "Arimo", sans-serif; font-weight: 700; font-size: 27px; color: var(--brand-deep); margin-top: 6px; }
  .contact-list { list-style: none; margin-top: 38px; margin-left: -20px; }
  .contact-list li { display: flex; align-items: center; gap: 6px; height: 29.5px; font-size: 20px; }
  .contact-list svg { width: 22px; height: 22px; flex: none; }

  .card-seam { position: absolute; left: 218px; top: 589px; width: 765px; height: 11px; background: linear-gradient(var(--seam), #b9babc); }

  /* Back */
  .card-back {
    top: 600px; height: 462px;
    background: radial-gradient(circle at 50% 42%, var(--back-glow) 0%, #eaebec 30%, var(--back-edge) 90%);
  }
  .back-brand {
    position: absolute; left: 0; right: 0; top: 188px;
    display: flex; justify-content: center; align-items: center; gap: 16px;
    color: var(--brand-blue); font-size: 46px; letter-spacing: 1px;
  }
  .back-brand .brand-dot { width: 30px; height: 30px; border-radius: 5px; }
  .back-url {
    position: absolute; left: 22px; right: 0; bottom: 14px;
    text-align: center; color: var(--brand-deep); font-size: 22px; letter-spacing: 26.5px;
  }
</style>
</head>
<body>

<section class="card card-front">
  <div class="front-header">
    <div class="brand-name"><span class="brand-dot"></span>Velvor IT Services</div>
    <span class="tile tile-blue" style="left:593px;top:27px;width:61px;height:61px;"></span>
    <span class="tile tile-blue" style="left:671px;top:67px;width:38px;height:38px;border-radius:7px;"></span>
    <span class="tile tile-blue" style="left:579px;top:123px;width:90px;height:90px;border-radius:12px;"></span>
    <span class="tile tile-blue" style="left:712px;top:18px;width:21px;height:21px;border-radius:3px;"></span>
  </div>

  <span class="tile tile-grey" style="left:191px;top:255px;width:90px;height:90px;border-radius:12px;"></span>
  <span class="tile tile-grey" style="left:150px;top:361px;width:39px;height:39px;border-radius:6px;"></span>
  <span class="tile tile-grey" style="left:206px;top:379px;width:61px;height:61px;border-radius:9px;"></span>
  <span class="tile tile-grey" style="left:128px;top:427px;width:20px;height:20px;border-radius:3px;"></span>

  <div class="contact-block">
    <p class="role">Director:</p>
    <p class="person-name">Marcus Dredge</p>
    <ul class="contact-list">
      <li>
        <svg viewBox="0 0 22 22" aria-hidden="true"><circle cx="11" cy="11" r="11" fill="#3b8fd6"/><path d="M7 6.5c1-.8 1.8-.3 2.2.6l.6 1.4c.2.6-.2 1-.7 1.3.5 1.2 1.4 2.1 2.6 2.7.3-.5.8-.9 1.3-.7l1.4.6c.9.4 1.3 1.2.6 2.1-1.6 1.7-4.2.4-6-1.5S5.4 8 7 6.5z" fill="#fff"/></svg>
        0483 906 452
      </li>
      <li>
        <svg viewBox="0 0 22 22" aria-hidden="true"><circle cx="11" cy="11" r="11" fill="#3b8fd6"/><rect x="5" y="7" width="12" height="8.5" rx="1" fill="#fff"/><path d="M5.4 7.4 11 12l5.6-4.6" fill="none" stroke="#3b8fd6" stroke-width="1.2"/></svg>
        support@velvorit.com.au
      </li>
      <li>
        <svg viewBox="0 0 22 22" aria-hidden="true"><circle cx="11" cy="11" r="11" fill="#3b8fd6"/><g fill="none" stroke="#fff" stroke-width="1.1"><circle cx="11" cy="11" r="6"/><ellipse cx="11" cy="11" rx="2.6" ry="6"/><path d="M5 11h12M6 8h10M6 14h10"/></g></svg>
        www.velvorit.com.au
      </li>
    </ul>
  </div>
</section>

<div class="card-seam"></div>

<section class="card card-back">
  <div class="back-brand"><span class="brand-dot"></span>Velvor IT Services</div>
  <p class="back-url">www.velvorit.com.au</p>
</section>

</body>
</html>
```